Young and modern Electrical company working in the commercial arena.

Wanting a business card design thats modern and will last. Maybe Minimalist? Happy to look at changing my logo

Target Market(s)

Builders, Project Managers

Industry/Entity Type

Electrical

Contact Information for Business Card

Name
Address
Phone number
Job title

Logo Text

our name or just the logo i'm open to ideas

Font styles to use
Sans Serif

Requirements
Nice to have
• would like to keep the purple in our current logo. it's kinda unique to our market
Should not have
• Don't want it to be to busy. simple is best i think

```html
<!DOCTYPE html>
<html lang="en">
<head>
<meta charset="utf-8">
<title>Harlow Electrical — Business Cards</title>
<link rel="stylesheet" href="https://fonts.googleapis.com/css2?family=Open+Sans:wght@400;600&display=swap">
<style>
  :root {
    --backdrop: #1d1d1f;
    --card-white: #f7f7f7;
    --panel-dark: #1c1e1c;
    --brand-purple: #7b4fc4;
    --ink: #2a2a2a;
    --name-light: #e6e6e6;
  }
  * { box-sizing: border-box; margin: 0; padding: 0; }
  html, body {
    width: 1200px; height: 660px; overflow: hidden;
    background: var(--backdrop);
    font-family: "Open Sans", sans-serif;
  }
  .canvas {
    position: relative; width: 1200px; height: 660px;
    display: flex; align-items: center; justify-content: center; gap: 60px;
  }
  .card {
    position: relative; width: 520px; height: 298px;
    background: var(--card-white);
    border-radius: 3px; overflow: hidden;
    box-shadow: 0 10px 30px rgba(0,0,0,.5);
  }

  /* Front */
  .card-front { display: flex; align-items: center; justify-content: center; }
  .wordmark {
    display: flex; align-items: center; gap: 12px;
    color: var(--brand-purple); font-weight: 600; font-size: 38px;
    letter-spacing: .5px; text-transform: lowercase;
  }
  .wordmark-square { width: 18px; height: 18px; background: var(--brand-purple); flex: none; }

  /* Back */
  .back-panel { position: absolute; inset: 0; width: 100%; height: 100%; }
  .back-brand { position: absolute; left: 34px; top: 40px; }
  .back-brand .wordmark { font-size: 22px; line-height: 23px; gap: 9px; letter-spacing: .3px; }
  .back-brand .wordmark-square { width: 12px; height: 12px; }
  .tagline {
    margin-top: 3px; margin-left: 21px;
    color: var(--brand-purple); font-size: 11px; font-weight: 400;
  }
  .holder { position: absolute; right: 56px; top: 70px; text-align: left; }
  .holder-name { color: var(--name-light); font-size: 22px; font-weight: 400; }
  .holder-name strong { font-weight: 600; }
  .holder-role { color: var(--brand-purple); font-size: 13px; margin-top: 2px; }

  .contact-list {
    position: absolute; left: 34px; bottom: 26px;
    list-style: none; display: flex; flex-direction: column; gap: 5px;
  }
  .contact-list li {
    display: flex; align-items: flex-start; gap: 8px;
    color: var(--ink); font-size: 12.5px; line-height: 16px;
  }
  .contact-icon {
    flex: none; width: 16px; height: 16px; border-radius: 50%;
    background: var(--brand-purple);
    display: flex; align-items: center; justify-content: center;
  }
  .contact-icon svg { width: 10px; height: 10px; }
</style>
</head>
<body>
<main class="canvas">

  <section class="card card-front" aria-label="Card front">
    <div class="wordmark"><span class="wordmark-square"></span>harlow electrical</div>
  </section>

  <section class="card card-back" aria-label="Card back">
    <svg class="back-panel" viewBox="0 0 520 298" preserveAspectRatio="none" aria-hidden="true">
      <polygon points="200,0 520,0 520,298 440,298" fill="var(--panel-dark)"/>
      <line x1="200" y1="0" x2="440" y2="298" stroke="var(--brand-purple)" stroke-width="3"/>
    </svg>

    <div class="back-brand">
      <div class="wordmark"><span class="wordmark-square"></span><span>harlow<br>electrical</span></div>
      <p class="tagline">Electrical Services</p>
    </div>

    <div class="holder">
      <p class="holder-name">Dana <strong>Kerr</strong></p>
      <p class="holder-role">Owner</p>
    </div>

    <ul class="contact-list">
      <li>
        <span class="contact-icon"><svg viewBox="0 0 10 10"><rect x="3" y="1" width="4" height="8" rx="0.8" fill="none" stroke="#fff" stroke-width="1"/></svg></span>
        0400 000 123
      </li>
      <li>
        <span class="contact-icon"><svg viewBox="0 0 10 10"><rect x="1.5" y="2.5" width="7" height="5" fill="none" stroke="#fff" stroke-width="1"/><polyline points="1.5,2.5 5,5.5 8.5,2.5" fill="none" stroke="#fff" stroke-width="1"/></svg></span>
        dana@harlowelectrical.com.au
      </li>
      <li>
        <span class="contact-icon"><svg viewBox="0 0 10 10"><circle cx="5" cy="5" r="3.5" fill="none" stroke="#fff" stroke-width="1"/><line x1="1.5" y1="5" x2="8.5" y2="5" stroke="#fff" stroke-width="0.8"/><ellipse cx="5" cy="5" rx="1.5" ry="3.5" fill="none" stroke="#fff" stroke-width="0.8"/></svg></span>
        www.harlowelectrical.com.au
      </li>
      <li>
        <span class="contact-icon"><svg viewBox="0 0 10 10"><path d="M5 9 C3 6.5 2.5 5.5 2.5 4 A2.5 2.5 0 0 1 7.5 4 C7.5 5.5 7 6.5 5 9 Z" fill="#fff"/><circle cx="5" cy="4" r="0.9" fill="var(--brand-purple)"/></svg></span>
        your address your address,<br>your address
      </li>
    </ul>
  </section>

</main>
</body>
</html>
```